Business Card Design for Brook and Vale Reporting Services

I would like a business card design for my new logo that you have done.
Info on first side will be the logo and the following info:
Gil Prowse, CEO & General Manager
12 Maple Crest Road
Ashford Bay, Ontario
P3K 1B8
Phone: (807)-555-3947
Toll Free: (844) 555-7093
Cell: (807) 555-2816
Fax: (807) 555-6104
emai: gil@brookvaletx.ca
www.brookvaletx.ca
On the second side:
We serve all of Northwestern Ontario
Services we offer:
Reporting Services for examination for discoveries, depositions, hearings, mediations, arbitration and conferences. Transcription Services.
As well: Process Serving, Remote/Mobile Signing and Court filing & Searches. We are a member of
(INSERT THE PASCUN logo here)
Process Serv
Target Market(s)
Law Firms and business corporations
Include din beief

```html
<!DOCTYPE html>
<html lang="en">
<head>
<meta charset="utf-8">
<title>Brook and Vale Reporting Services – Business Card</title>
<link rel="stylesheet" href="https://fonts.googleapis.com/css2?family=Montserrat:ital,wght@0,400;0,600;0,700;1,400&display=swap">
<style>
  :root {
    --navy: #1f3370;
    --navy-deep: #1a2b60;
    --gold: #d9a02b;
    --white: #ffffff;
    --ink: #2b2b2b;
    --page: #ecebe7;
  }
  * { margin: 0; padding: 0; box-sizing: border-box; }
  html, body { width: 1200px; height: 1023px; overflow: hidden; }
  body {
    background: var(--page);
    font-family: "Montserrat", Arial, sans-serif;
    position: relative;
  }
  .card {
    position: absolute;
    left: 206px;
    width: 788px;
    height: 450px;
    border-radius: 18px;
    overflow: hidden;
    box-shadow: 0 4px 14px rgba(0,0,0,0.15);
  }
  /* Front */
  .card-front { top: 40px; background: var(--white); }
  .front-logo {
    position: absolute; left: 30px; top: 0; width: 350px; height: 100%;
    display: flex; align-items: center; justify-content: center; gap: 14px;
  }
  .logo-dot {
    width: 22px; height: 22px; border-radius: 50%;
    background: var(--gold); flex: none;
  }
  .logo-name {
    font-weight: 700; color: var(--navy); font-size: 25px; line-height: 1.15;
    text-transform: uppercase; letter-spacing: 0.5px;
  }
  .front-divider {
    position: absolute; left: 404px; top: 70px; width: 2px; height: 310px;
    background: var(--navy);
  }
  .front-info { position: absolute; left: 436px; top: 66px; right: 30px; color: var(--ink); }
  .person-name { font-weight: 700; color: var(--navy); font-size: 30px; }
  .person-title { font-size: 16px; margin-top: 4px; }
  .address { font-size: 16px; margin-top: 18px; line-height: 1.45; }
  .contact-list { list-style: none; margin-top: 14px; font-size: 16px; line-height: 1.75; }
  .contact-list li { display: flex; align-items: center; gap: 10px; white-space: nowrap; }
  .contact-list svg { width: 16px; height: 16px; fill: var(--gold); flex: none; }

  /* Back */
  .card-back { top: 530px; background: var(--navy); color: var(--white); text-align: center; }
  .back-logo {
    position: absolute; top: 34px; left: 0; right: 0;
    display: flex; align-items: center; justify-content: center; gap: 14px;
  }
  .back-logo .logo-name { color: var(--white); font-size: 30px; }
  .service-band {
    position: absolute; top: 150px; left: 0; right: 0; height: 44px;
    background: var(--gold); color: var(--navy-deep);
    font-weight: 700; font-size: 22px; line-height: 44px; letter-spacing: 0.5px;
  }
  .services { position: absolute; top: 216px; left: 40px; right: 40px; }
  .services-heading { font-weight: 700; font-size: 20px; letter-spacing: 0.5px; }
  .services-text { font-style: italic; font-size: 16px; line-height: 1.5; margin-top: 10px; }
  .member-line { font-style: italic; font-size: 16px; margin-top: 6px; }
  .member-mark {
    display: inline-flex; align-items: center; gap: 8px; margin-top: 10px;
    font-weight: 700; font-size: 17px; letter-spacing: 1px;
  }
  .member-square { width: 16px; height: 16px; background: var(--white); }
</style>
</head>
<body>

<section class="card card-front" aria-label="Card front">
  <div class="front-logo">
    <span class="logo-dot"></span>
    <span class="logo-name">Brook and Vale<br>Reporting<br>Services Inc.</span>
  </div>
  <div class="front-divider"></div>
  <div class="front-info">
    <p class="person-name">Gil Prowse</p>
    <p class="person-title">CEO &amp; General Manager</p>
    <p class="address">12 Maple Crest Road<br>Ashford Bay, Ontario, P3K 1B8</p>
    <ul class="contact-list">
      <li><svg viewBox="0 0 16 16"><path d="M4 1l2.5 3-1.5 2c1 2 3 4 5 5l2-1.5 3 2.5-2 2.5C7 15 1 9 1.5 3.5z"/></svg>(807)-555-3947</li>
      <li><svg viewBox="0 0 16 16"><path d="M4 1l2.5 3-1.5 2c1 2 3 4 5 5l2-1.5 3 2.5-2 2.5C7 15 1 9 1.5 3.5z"/></svg>(844) 555-7093 (Toll Free)</li>
      <li><svg viewBox="0 0 16 16"><path d="M4.5 0h7a1.5 1.5 0 0 1 1.5 1.5v13a1.5 1.5 0 0 1-1.5 1.5h-7A1.5 1.5 0 0 1 3 14.5v-13A1.5 1.5 0 0 1 4.5 0zM5 2v10h6V2z"/></svg>(807) 555-2816</li>
      <li><svg viewBox="0 0 16 16"><path d="M4 0h8v4H4zM1 5h14v7h-3v4H4v-4H1zM5 10v4h6v-4z"/></svg>(807) 555-6104</li>
      <li><svg viewBox="0 0 16 16"><path d="M0 3h16v10H0zM1.5 4.5L8 9l6.5-4.5v-.5h-13z"/></svg>gil@brookvaletx.ca</li>
      <li><svg viewBox="0 0 16 16"><path d="M8 0a8 8 0 1 0 0 16A8 8 0 0 0 8 0zm0 2a6 6 0 0 1 0 12A6 6 0 0 1 8 2zM2 7.3h12v1.4H2z"/></svg>www.brookvaletx.ca</li>
    </ul>
  </div>
</section>

<section class="card card-back" aria-label="Card back">
  <div class="back-logo">
    <span class="logo-dot"></span>
    <span class="logo-name">Brook and Vale<br>Reporting Services Inc.</span>
  </div>
  <p class="service-band">WE SERVE ALL OF THE NORTHWESTERN ONTARIO</p>
  <div class="services">
    <p class="services-heading">SERVICES WE OFFER</p>
    <p class="services-text">Reporting Services for examination for discoveries, depositions, hearings, mediations, arbitration and conferences. Transcription Services.<br>As well: Process Serving, Remote/Mobile Signing and Court filing &amp; Searches.</p>
    <p class="member-line">We are a member of</p>
    <span class="member-mark"><span class="member-square"></span>PASCUN</span>
  </div>
</section>

</body>
</html>
```